Mara Joss Advisory Business Cards

Hi - using the information and logo provided I require a two sided business card designed with the following information. The business card is a 'mini card' 3.5" x 1.25".

Front of card should be the logo attached but inverted (so the background is the peach colour and the logo white).

Back should have these details. If we can't fit the Instragram and Facebook part can we just put the little logos.

Ruth Penderby

Art and Design Consultant
Dealer - Curator - Events - Styling - Creative Sourcing

P: 0462 913 058
E: ruth@marajossadvisory.example
W: www.marajossadvisory.example
I (instagram image please): marajossadvisory F (Facebook image please): MaraJossAdvisor

Target Market(s)

Galleries, artists, art buyers, interior design clients, event managers, creative types

Industry/Entity Type

Business

```html
<!DOCTYPE html>
<html lang="en">
<head>
<meta charset="utf-8">
<title>Mara Joss Advisory – Business Card</title>
<link rel="stylesheet" href="https://fonts.googleapis.com/css2?family=Cabin:wght@400&family=Tinos:ital@1&display=swap">
<style>
  :root {
    --peach: #f4b99d;
    --peach-line: #f6c6ae;
    --ink: #6d6e70;
    --paper: #ffffff;
  }
  * { margin: 0; padding: 0; box-sizing: border-box; }
  html, body {
    width: 1200px;
    height: 1000px;
    overflow: hidden;
    background: var(--paper);
  }
  .canvas {
    position: relative;
    width: 1200px;
    height: 1000px;
  }
  .card-front {
    position: absolute;
    left: 74px;
    top: 56px;
    width: 1051px;
    height: 374px;
    background: var(--peach);
  }
  .brand-mark {
    position: absolute;
    left: 50%;
    top: 67px;
    width: 120px;
    height: 120px;
    margin-left: -60px;
    border-radius: 50%;
    background: var(--paper);
  }
  .brand-name {
    position: absolute;
    left: 0;
    right: 0;
    top: 248px;
    text-align: center;
    font-family: "Cabin", sans-serif;
    font-weight: 400;
    font-size: 38px;
    letter-spacing: 0.22em;
    text-transform: uppercase;
    color: var(--ink);
  }
  .card-back {
    position: absolute;
    left: 74px;
    top: 558px;
    width: 1051px;
    height: 376px;
    border: 1px solid var(--peach-line);
    background: var(--paper);
  }
  .person-name {
    position: absolute;
    left: 58px;
    top: 52px;
    font-family: "Cabin", sans-serif;
    font-weight: 400;
    font-size: 36px;
    color: var(--ink);
  }
  .roles {
    position: absolute;
    left: 58px;
    top: 120px;
    font-family: "Tinos", serif;
    font-style: italic;
    font-size: 22px;
    line-height: 29px;
    color: var(--peach);
  }
  .contact-list {
    position: absolute;
    left: 58px;
    top: 196px;
    list-style: none;
    font-family: "Cabin", sans-serif;
    font-size: 21px;
    line-height: 33.5px;
    color: var(--ink);
  }
  .social-row {
    display: flex;
    align-items: center;
  }
  .social-item {
    display: flex;
    align-items: center;
  }
  .social-item + .social-item { margin-left: 50px; }
  .social-square {
    width: 30px;
    height: 30px;
    border-radius: 4px;
    background: var(--peach);
    margin-right: 10px;
  }
</style>
</head>
<body>
<main class="canvas">
  <section class="card-front">
    <div class="brand-mark" aria-hidden="true"></div>
    <p class="brand-name">Mara Joss Advisory</p>
  </section>

  <section class="card-back">
    <h1 class="person-name">Ruth Penderby</h1>
    <p class="roles">Art and Design Consultant<br>Dealer - Curator - Events - Styling - Creative Sourcing</p>
    <ul class="contact-list">
      <li>P: 0462 913 058</li>
      <li>E: ruth@marajossadvisory.example</li>
      <li>W: www.marajossadvisory.example</li>
      <li class="social-row">
        <span class="social-item"><span class="social-square" aria-hidden="true"></span>marajossadvisory</span>
        <span class="social-item"><span class="social-square" aria-hidden="true"></span>MaraJossAdvisor</span>
      </li>
    </ul>
  </section>
</main>
</body>
</html>
```